Poster Needed for Church Conference

I need a poster for a weekend conference at my church. Looking to attract as many people as possible. We are a church in the suburbs of Houston. This is mainly for our own church members but we are opening it up to outside church members.

Please see previous design from last conference and all other graphic work that can (doesn't need to be) included.

Target Market(s)

It's targeted for all people. But our main audience is families. around the age of 30 should be main target.

Industry/Entity Type

Non-Profit

Font styles to use
Serif
Sans Serif

Colors

Designer to choose colors to be used in the design.

Requirements
Must have
• 11x17 design with ability to shrink and blow up. but ideally for 11x17
• Content and wording:
• "Rooted Lantern Conference: Bridging the gap between generations and passing on our deepest beliefs and values."
• Featuring Dr. Glen Marlowe. Author of "The Map of Q9"
• Aug 25-26: Friday 8-10 pm, Saturday 4-8 pm
• Cost Adults $15/Children $5: Covers admission to all sessions and workshops, refreshments and Saturday dinner. *kids 5 and under free
• Childcare provided for all sessions. "
• Please use church logo and address on flyer: 4312 Orchard Bend, Missouri City, TX 77512
Nice to have
• Ideally it will be designed so that we can crop a 16:9 pp announcement slide and header for our website.
Should not have
• anything offensive

```html
<!DOCTYPE html>
<html lang="en">
<head>
<meta charset="utf-8">
<title>Rooted Lantern Conference</title>
<link rel="stylesheet" href="https://fonts.googleapis.com/css2?family=Source+Sans+3:wght@400;600;700&display=swap">
<style>
  :root {
    --sky-top: #3f7fc4;
    --sky-mid: #8fb8e2;
    --sky-haze: #dfe9ef;
    --hills: #6e9a3c;
    --forest: #4e7a22;
    --door-dark: #3b3a38;
    --door-light: #6d6963;
    --white: #ffffff;
    --ink: #1b1b1b;
    --date-green: #6cbd1f;
    --time-blue: #1c4f9c;
  }
  * { box-sizing: border-box; margin: 0; padding: 0; }
  html, body { width: 1200px; height: 776px; overflow: hidden; }
  body { font-family: "Source Sans 3", "Source Sans Pro", sans-serif; background: var(--white); }

  .poster { position: relative; width: 1200px; height: 776px; overflow: hidden; }

  .scene-view {
    position: absolute; inset: 0;
    background: linear-gradient(180deg,
      var(--sky-top) 0%, var(--sky-mid) 38%, var(--sky-haze) 66%,
      var(--hills) 78%, var(--forest) 100%);
  }
  .door {
    position: absolute; top: 0; height: 776px;
    background: linear-gradient(90deg, var(--door-dark), var(--door-light) 50%, var(--door-dark));
  }
  .door--left { left: 0; width: 242px; }
  .door--right { right: 0; width: 242px; }

  .content { position: absolute; inset: 0; text-align: center; }
  .content > * { position: absolute; left: 0; right: 0; }

  .title {
    top: 22px; color: var(--white); font-weight: 700;
    font-size: 84px; line-height: 84px; letter-spacing: 0.5px; text-transform: uppercase;
  }
  .tagline {
    top: 192px; color: var(--white); font-weight: 700;
    font-size: 29px; line-height: 31px;
  }
  .featuring-label { top: 272px; color: var(--ink); font-weight: 700; font-size: 17px; }
  .speaker { top: 299px; color: var(--ink); font-weight: 700; font-size: 24px; }

  .date-badge {
    top: 343px; left: 423px; right: auto; width: 363px; height: 72px;
    background: var(--date-green); color: var(--white);
    font-weight: 700; font-size: 48px; line-height: 72px;
  }
  .times { top: 420px; color: var(--time-blue); font-weight: 700; font-size: 34px; }
  .cost-heading { top: 471px; color: var(--ink); font-weight: 700; font-size: 29px; }
  .cost-prices { top: 505px; color: var(--ink); font-weight: 400; font-size: 24px; }
  .cost-details { top: 539px; color: var(--ink); font-size: 18px; line-height: 20px; }
  .childcare { top: 580px; color: var(--ink); font-size: 18px; }

  .church-name {
    top: 640px; color: var(--white); font-weight: 700;
    font-size: 34px; line-height: 40px;
  }
  .address { top: 737px; color: var(--white); font-weight: 700; font-size: 18px; }
</style>
</head>
<body>
<main class="poster">
  <div class="scene-view" role="img" aria-label="Photo of a bright blue sky with clouds over green forested hills"></div>
  <div class="door door--left" role="img" aria-label="Photo of a weathered wooden door being pushed open by a hand"></div>
  <div class="door door--right" role="img" aria-label="Photo of a weathered wooden door being pushed open by a hand"></div>

  <section class="content">
    <h1 class="title">Rooted Lantern<br>Conference</h1>
    <p class="tagline">Bridging the gap between generations and<br>passing on our deepest beliefs and values.</p>
    <p class="featuring-label">FEATURING</p>
    <p class="speaker">Dr. Glen Marlowe. Author of "The Map of Q9"</p>
    <p class="date-badge">Aug 25-26</p>
    <p class="times">Friday 8-10 pm, Saturday 4-8 pm</p>
    <h2 class="cost-heading">Cost</h2>
    <p class="cost-prices">Adults $15/Children $5</p>
    <p class="cost-details">Covers admission to all sessions and workshops,<br>refreshments and Saturday dinner. *kids 5 and under free</p>
    <p class="childcare">Childcare provided for all sessions.</p>
    <p class="church-name">Cedar Hollow<br>Community Church</p>
    <p class="address">4312 Orchard Bend, Missouri City, TX 77512</p>
  </section>
</main>
</body>
</html>
```